Silver Lumen Med Spa Membership Sales Presentation to Clients handout

Hello! We are a high tech, Silver Lumen Med Spa in Dallas Texas that won Best Med Spa in Addison. I want my graphic membership form to represent that. We serve women and men so want it neutral but show cutting edge. Our colors are black, white, gray but would entertain your view. Having a challenge on making it easy to read as each membership gets more services yet one service a month. Thought maybe colorcoding what services are together? Definite road blocks on my end. I used Canva to lay out, but as you can see I am NOT gifted at graphic design. ;))

Target Market(s)

39-69

Industry/Entity Type

Medical Med Spa

Requirements
Must have
• cutting edge look

```html
<!DOCTYPE html>
<html lang="en">
<head>
<meta charset="utf-8">
<title>Silver Lumen Med Spa – Ageless Glow Membership</title>
<link href="https://fonts.googleapis.com/css2?family=Poppins:ital,wght@0,300;0,400;0,700;0,800;1,400;1,800&display=swap" rel="stylesheet">
<style>
  :root{
    --black:#000;
    --white:#fff;
    --ink:#1a1a1a;
    --grey:#b3b3b3;
    --grey-cap:#a9a9a9;
    --rule:#e2e2e2;
    --rule-dark:#3a3a3a;
    --tick:#14a84a;
    --deal:#d0021b;
    --award:#c8102e;
  }
  *{margin:0;padding:0;box-sizing:border-box}
  html,body{width:924px;height:1200px;overflow:hidden;background:var(--white)}
  body{font-family:"Poppins",sans-serif;color:var(--ink)}
  .sheet{position:relative;width:924px;height:1200px;background:var(--white);overflow:hidden}

  /* header */
  .masthead{position:absolute;left:0;top:0;width:924px;height:234px;background:var(--black)}
  .brand-name{position:absolute;left:64px;top:118px;font-family:"Poppins",sans-serif;font-weight:300;font-size:20px;letter-spacing:1px;color:#d9d9d9}
  .program-title{position:absolute;left:62px;top:172px;font-family:"Poppins",sans-serif;font-weight:800;font-style:italic;font-size:28px;letter-spacing:.3px;color:var(--white)}
  .award-badge{position:absolute;left:755px;top:48px;width:88px;height:88px}

  /* highlighted tier column */
  .better-column{position:absolute;left:572px;top:222px;width:148px;height:941px;background:var(--black)}
  .better-column::before{content:"";position:absolute;left:0;top:0;width:100%;height:12px;background:var(--grey-cap)}
  .better-column::after{content:"";position:absolute;left:0;top:95px;width:100%;height:1px;background:#555}

  /* table head */
  .table-title{position:absolute;left:64px;top:252px}
  .table-title h2{font-weight:700;font-size:17px;letter-spacing:.3px;color:var(--black)}
  .table-title p{font-style:italic;font-size:8px;color:var(--ink);margin-top:1px}
  .tier{position:absolute;top:248px;width:120px;text-align:center}
  .tier .tier-name{font-weight:400;font-size:18px;letter-spacing:.5px}
  .tier .tier-price{font-weight:700;font-size:21px;margin-top:4px;line-height:1}
  .tier .tier-price sup{font-weight:400;font-size:9px;vertical-align:top;margin-right:3px}
  .tier-good{left:439px}
  .tier-better{left:586px;top:243px;color:var(--white)}
  .tier-best{left:739px;top:245px}

  /* rows */
  .treatments{position:absolute;left:0;top:317px;width:924px}
  .row{display:grid;grid-template-columns:60px 363px 36px 80px 67px 80px 73px 80px;height:28.1px;align-items:center}
  .row.deal{height:25.8px}
  .label{grid-column:2;font-size:12.5px;color:var(--ink);height:100%;display:flex;align-items:center;padding-left:6px;border-bottom:1px solid var(--rule)}
  .row:last-child .label{border-bottom:none}
  .cell{height:100%;display:flex;align-items:center;justify-content:center;position:relative;font-size:15px}
  .cell::after{content:"";position:absolute;left:4px;right:4px;bottom:0;height:1px;background:linear-gradient(90deg,transparent,var(--rule) 30%,var(--rule) 70%,transparent)}
  .cell.c-good{grid-column:4}
  .cell.c-better{grid-column:6}
  .cell.c-better::after{background:linear-gradient(90deg,transparent,var(--rule-dark) 30%,var(--rule-dark) 70%,transparent)}
  .cell.c-best{grid-column:8}
  .yes{color:var(--tick);font-weight:400}
  .no{color:#888;font-size:13px}
  .c-better .no{color:var(--white)}
  .off{color:var(--deal);font-weight:700;font-size:12px;letter-spacing:.2px}

  /* buttons */
  .join{position:absolute;top:1118px;width:74px;height:19px;border-radius:10px;font-size:7.5px;display:flex;align-items:center;justify-content:center;color:var(--white);background:var(--black)}
  .join-good{left:462px}
  .join-better{left:609px;background:#9a9a9a}
  .join-best{left:762px;top:1120px}

  /* footer */
  .footer-band{position:absolute;left:0;top:1163px;width:924px;height:34px;background:var(--grey);border-bottom:3px solid #d7d7d7}
  .contact{position:absolute;top:1168px;display:flex;align-items:center;gap:10px;font-size:11px;color:var(--ink)}
  .contact .icon{width:24px;height:24px;border-radius:50%;background:var(--white);display:flex;align-items:center;justify-content:center;box-shadow:0 0 0 2px #d0d0d0}
  .contact-address{left:50px}
  .contact-phone{left:392px}
  .website{position:absolute;left:750px;top:1155px;width:174px;height:34px;background:var(--black);clip-path:polygon(0 0,100% 0,100% 100%,22px 100%);color:var(--white);font-size:10px;display:flex;align-items:center;justify-content:flex-end;padding-right:16px}
</style>
</head>
<body>
<div class="sheet">

  <header class="masthead">
    <div class="brand-name">Silver Lumen Med Spa</div>
    <h1 class="program-title">AGELESS GLOW&nbsp; MEMBERSHIP</h1>
    <svg class="award-badge" viewBox="0 0 88 88" role="img" aria-label="Award badge">
      <circle cx="44" cy="44" r="41" fill="#111" stroke="var(--award)" stroke-width="4"/>
    </svg>
  </header>

  <div class="better-column"></div>

  <div class="table-title">
    <h2>TREATMENTS</h2>
    <p>GREEN UNLIMITED /CHOSE ONE COLOUR PER MONTH</p>
  </div>
  <div class="tier tier-good"><div class="tier-name">GOOD</div><div class="tier-price"><sup>$</sup>189</div></div>
  <div class="tier tier-better"><div class="tier-name">BETTER</div><div class="tier-price"><sup>$</sup>289</div></div>
  <div class="tier tier-best"><div class="tier-name">BEST</div><div class="tier-price"><sup>$</sup>389</div></div>

  <section class="treatments">
    <div class="row"><div class="label">Skin Evaluation</div><div class="cell c-good yes">✓</div><div class="cell c-better yes">✓</div><div class="cell c-best yes">✓</div></div>
    <div class="row"><div class="label">Infrared Sauna</div><div class="cell c-good yes">✓</div><div class="cell c-better yes">✓</div><div class="cell c-best yes">✓</div></div>
    <div class="row"><div class="label">Massage Chair</div><div class="cell c-good yes">✓</div><div class="cell c-better yes">✓</div><div class="cell c-best yes">✓</div></div>
    <div class="row"><div class="label">Vibrational Lymphatic Plate</div><div class="cell c-good yes">✓</div><div class="cell c-better yes">✓</div><div class="cell c-best yes">✓</div></div>
    <div class="row"><div class="label">Medical Facial</div><div class="cell c-good yes">✓</div><div class="cell c-better yes">✓</div><div class="cell c-best yes">✓</div></div>
    <div class="row"><div class="label">Face Lymphatic Drainage</div><div class="cell c-good yes">✓</div><div class="cell c-better yes">✓</div><div class="cell c-best yes">✓</div></div>
    <div class="row"><div class="label">Red Light Therapy</div><div class="cell c-good yes">✓</div><div class="cell c-better yes">✓</div><div class="cell c-best yes">✓</div></div>
    <div class="row"><div class="label">Ph Oxygen Serum</div><div class="cell c-good yes">✓</div><div class="cell c-better yes">✓</div><div class="cell c-best yes">✓</div></div>
    <div class="row"><div class="label">Chemical Peels Progressive Or Middepth</div><div class="cell c-good yes">✓</div><div class="cell c-better yes">✓</div><div class="cell c-best yes">✓</div></div>
    <div class="row"><div class="label">Lumis IPL Ageless Glow</div><div class="cell c-good yes">✓</div><div class="cell c-better yes">✓</div><div class="cell c-best yes">✓</div></div>
    <div class="row"><div class="label">Lumis 2 Correction Passes</div><div class="cell c-good yes">✓</div><div class="cell c-better yes">✓</div><div class="cell c-best yes">✓</div></div>
    <div class="row"><div class="label">Dermaplaning</div><div class="cell c-good no">–</div><div class="cell c-better yes">✓</div><div class="cell c-best yes">✓</div></div>
    <div class="row"><div class="label">Vitamin A Peel</div><div class="cell c-good no">–</div><div class="cell c-better yes">✓</div><div class="cell c-best yes">✓</div></div>
    <div class="row"><div class="label">Lumis Up To 10 Correction Passes</div><div class="cell c-good no">–</div><div class="cell c-better yes">✓</div><div class="cell c-best yes">✓</div></div>
    <div class="row"><div class="label">Lumis 2 Correction Passes</div><div class="cell c-good no">–</div><div class="cell c-better yes">✓</div><div class="cell c-best yes">✓</div></div>
    <div class="row"><div class="label">Microneedling</div><div class="cell c-good no">–</div><div class="cell c-better yes">✓</div><div class="cell c-best yes">✓</div></div>
    <div class="row"><div class="label">Lumis Skin Tight</div><div class="cell c-good no">–</div><div class="cell c-better no">–</div><div class="cell c-best yes">✓</div></div>
    <div class="row"><div class="label">Microneedling PDO Radiance</div><div class="cell c-good no">–</div><div class="cell c-better no">–</div><div class="cell c-best yes">✓</div></div>
    <div class="row"><div class="label">Chemical Peel Ivory Italian</div><div class="cell c-good no">–</div><div class="cell c-better no">–</div><div class="cell c-best yes">✓</div></div>
    <div class="row"><div class="label">Contour Targeted Weight Loss</div><div class="cell c-good no">–</div><div class="cell c-better no">–</div><div class="cell c-best yes">✓</div></div>

    <div class="row deal"><div class="label">Laser Rejuvenation</div><div class="cell c-good off">10% OFF</div><div class="cell c-better off">20% OFF</div><div class="cell c-best off">30% OFF</div></div>
    <div class="row deal"><div class="label">Plasma Pen</div><div class="cell c-good off">10% OFF</div><div class="cell c-better off">20% OFF</div><div class="cell c-best off">30% OFF</div></div>
    <div class="row deal"><div class="label">Hyperbaric Oxygen</div><div class="cell c-good off">10% OFF</div><div class="cell c-better off">20% OFF</div><div class="cell c-best off">30% OFF</div></div>
    <div class="row deal"><div class="label">Massage</div><div class="cell c-good off">10% OFF</div><div class="cell c-better off">20% OFF</div><div class="cell c-best off">30% OFF</div></div>
    <div class="row deal"><div class="label">Airbrush Tanning</div><div class="cell c-good off">10% OFF</div><div class="cell c-better off">20% OFF</div><div class="cell c-best off">30% OFF</div></div>
    <div class="row deal"><div class="label">Ionic Detox</div><div class="cell c-good off">10% OFF</div><div class="cell c-better off">20% OFF</div><div class="cell c-best off">30% OFF</div></div>
    <div class="row deal"><div class="label">Lymphatic Drainage</div><div class="cell c-good off">10% OFF</div><div class="cell c-better off">20% OFF</div><div class="cell c-best off">30% OFF</div></div>
    <div class="row deal"><div class="label">Tirzepatide Weight Loss Peptide</div><div class="cell c-good off">10% OFF</div><div class="cell c-better off">20% OFF</div><div class="cell c-best off">30% OFF</div></div>
    <div class="row deal"><div class="label">Lip Fillers Needle-less</div><div class="cell c-good off">10% OFF</div><div class="cell c-better off">20% OFF</div><div class="cell c-best off">30% OFF</div></div>
  </section>

  <div class="join join-good">Try know</div>
  <div class="join join-better">Try know</div>
  <div class="join join-best">Try know</div>

  <footer>
    <div class="footer-band"></div>
    <div class="contact contact-address">
      <span class="icon"><svg width="12" height="14" viewBox="0 0 12 14"><path d="M6 0C2.7 0 0 2.6 0 5.8 0 10 6 14 6 14s6-4 6-8.2C12 2.6 9.3 0 6 0zm0 8a2.2 2.2 0 1 1 0-4.4A2.2 2.2 0 0 1 6 8z" fill="#111"/></svg></span>
      <span>1180 Harlow Ave. Plano, TX 75093</span>
    </div>
    <div class="contact contact-phone">
      <span class="icon"><svg width="12" height="12" viewBox="0 0 24 24"><path d="M6.6 10.8a15.1 15.1 0 0 0 6.6 6.6l2.2-2.2c.3-.3.7-.4 1-.2 1.1.4 2.3.6 3.6.6.6 0 1 .4 1 1V20c0 .6-.4 1-1 1A17 17 0 0 1 3 4c0-.6.4-1 1-1h3.5c.6 0 1 .4 1 1 0 1.3.2 2.5.6 3.6.1.3 0 .7-.2 1z" fill="#111"/></svg></span>
      <span>214.555.0142</span>
    </div>
    <div class="website">SilverLumenMedSpa.com</div>
  </footer>

</div>
</body>
</html>
```